fizzy drinks label design

I want to design fizzy drink label for 3 flavors : black grapes, red apple and mojito, band name kestrola, product name KOLTA , product will be in plastic bottle, label size 198 mm X 66mm

```html
<!DOCTYPE html>
<html lang="en">
<head>
<meta charset="utf-8">
<title>KOLTA fizzy drink labels</title>
<link rel="stylesheet" href="https://fonts.googleapis.com/css2?family=Amatic+SC:wght@700&family=Bebas+Neue&display=swap">
<style>
  :root {
    --page: #e6e6e6;
    --paper: #ffffff;
    --mojito: #3f8a12;
    --mojito-soft: #9fd05a;
    --grape: #3a1f45;
    --grape-soft: #5a5a8a;
    --apple: #cc0f0f;
    --apple-soft: #f26a2a;
    --leaf: #4f9a3a;
  }
  * { margin: 0; padding: 0; box-sizing: border-box; }
  html, body { width: 1200px; height: 1200px; overflow: hidden; background: var(--page); }
  .sheet { position: relative; width: 1200px; height: 1200px; }

  .label {
    position: absolute; left: 249px; width: 702px; height: 237px;
    background: var(--paper); border-radius: 3px; overflow: hidden;
    box-shadow: 0 1px 3px rgba(0,0,0,.18);
  }
  .label--mojito { top: 172px; --accent: var(--mojito); --soft: var(--mojito-soft); }
  .label--grape  { top: 481px; --accent: var(--grape);  --soft: var(--grape-soft); }
  .label--apple  { top: 766px; --accent: var(--apple);  --soft: var(--apple-soft); }

  .brand-tab {
    position: absolute; left: 308px; top: 2px; width: 65px; height: 62px;
    background: var(--accent); display: flex; align-items: center; justify-content: center;
  }
  .brand-tab__name {
    font-family: "Bebas Neue", sans-serif; font-size: 17px; color: #fff; letter-spacing: .5px;
  }

  .streaks { position: absolute; left: 251px; top: 40px; width: 186px; height: 42px; }
  .streaks polygon { fill: var(--accent); }

  .hero-fruit {
    position: absolute; left: 242px; top: 67px; width: 183px; height: 152px; border-radius: 48% 52% 46% 54%;
    background: radial-gradient(circle at 45% 55%, var(--soft) 0%, var(--soft) 45%, rgba(255,255,255,0) 75%);
  }
  .label--mojito .hero-fruit {
    background: radial-gradient(circle at 45% 60%, #c9e46a 0%, #6fb43a 40%, rgba(111,180,58,.25) 65%, rgba(255,255,255,0) 78%);
  }
  .label--grape .hero-fruit {
    background: radial-gradient(ellipse at 50% 50%, #2a2440 0%, #4a4870 40%, rgba(90,90,138,.3) 65%, rgba(255,255,255,0) 78%);
  }
  .label--apple .hero-fruit {
    background: radial-gradient(circle at 50% 55%, #f5862e 0%, #e5361a 40%, rgba(229,54,26,.25) 65%, rgba(255,255,255,0) 78%);
  }

  .product-name {
    position: absolute; left: 262px; top: 90px; width: 150px; text-align: center;
    font-family: "Amatic SC", sans-serif; font-weight: 700; font-size: 88px; line-height: 1;
    color: #fff;
  }

  .flavour {
    position: absolute; right: 223px; top: 175px; text-align: right;
    font-family: "Bebas Neue", sans-serif; font-size: 25px; line-height: 1; color: var(--accent);
  }
  .tagline {
    position: absolute; right: 220px; top: 196px;
    font-family: "Amatic SC", sans-serif; font-weight: 700; font-size: 33px; line-height: 1; color: var(--accent);
  }
  .volume {
    position: absolute; left: 253px; top: 206px;
    font-family: "Bebas Neue", sans-serif; font-size: 15px; line-height: 1; color: var(--accent);
  }
  .label--apple .volume { color: #111; }
  .label--grape .volume { color: var(--grape); }

  .garnish { position: absolute; border-radius: 50%; }
  .label--mojito .garnish { background: radial-gradient(circle at 55% 45%, #c8e36a 0%, #7cc04a 45%, rgba(79,154,58,.35) 70%, rgba(255,255,255,0) 80%); }
  .label--grape .garnish { border-radius: 45% 55% 60% 40%; background: radial-gradient(ellipse at 50% 45%, #2c2a48 0%, #4f4e7a 50%, rgba(79,78,122,.3) 72%, rgba(255,255,255,0) 82%); }
  .label--apple .garnish { background: radial-gradient(circle at 45% 55%, #f7862f 0%, #e23a1c 45%, rgba(226,58,28,.3) 70%, rgba(255,255,255,0) 80%); }

  .g1 { left: 2px; top: 3px; width: 65px; height: 60px; }
  .g2 { left: 152px; top: 42px; width: 87px; height: 76px; }
  .g3 { left: 34px; top: 168px; width: 50px; height: 59px; }
  .g4 { left: 486px; top: 41px; width: 42px; height: 47px; }
  .g5 { left: 489px; top: 128px; width: 83px; height: 71px; }
  .g6 { left: 658px; top: 14px; width: 40px; height: 48px; }
  .g7 { left: 643px; top: 179px; width: 58px; height: 56px; }
</style>
</head>
<body>
<main class="sheet">

  <section class="label label--mojito" aria-label="KOLTA mojito label">
    <div class="garnish g1" role="img" aria-label="Lime slices with mint leaves"></div>
    <div class="garnish g2" role="img" aria-label="Lime slices with mint leaves"></div>
    <div class="garnish g3" role="img" aria-label="Lime slice with mint leaves"></div>
    <div class="garnish g4" role="img" aria-label="Lime slice with mint leaves"></div>
    <div class="garnish g5" role="img" aria-label="Lime slices with mint leaves"></div>
    <div class="garnish g6" role="img" aria-label="Lime slice with mint leaves"></div>
    <div class="garnish g7" role="img" aria-label="Lime slice with mint leaves"></div>
    <div class="brand-tab"><span class="brand-tab__name">kestrola</span></div>
    <svg class="streaks" viewBox="0 0 186 42" aria-hidden="true"><polygon points="0,40 150,6 40,34"/><polygon points="20,42 186,2 60,34"/></svg>
    <div class="hero-fruit" role="img" aria-label="Watercolour lime wedge and mint leaves on halftone dots"></div>
    <p class="product-name">KOLTA</p>
    <p class="volume">200ml</p>
    <p class="flavour">MOJITO</p>
    <p class="tagline">fizzy drink</p>
  </section>

  <section class="label label--grape" aria-label="KOLTA black grapes label">
    <div class="garnish g1" role="img" aria-label="Bunch of black grapes"></div>
    <div class="garnish g2" role="img" aria-label="Bunch of black grapes"></div>
    <div class="garnish g3" role="img" aria-label="Bunch of black grapes"></div>
    <div class="garnish g4" role="img" aria-label="Bunch of black grapes"></div>
    <div class="garnish g5" role="img" aria-label="Bunch of black grapes"></div>
    <div class="garnish g6" role="img" aria-label="Bunch of black grapes"></div>
    <div class="garnish g7" role="img" aria-label="Bunch of black grapes"></div>
    <div class="brand-tab"><span class="brand-tab__name">kestrola</span></div>
    <svg class="streaks" viewBox="0 0 186 42" aria-hidden="true"><polygon points="0,40 150,6 40,34"/><polygon points="20,42 186,2 60,34"/></svg>
    <div class="hero-fruit" role="img" aria-label="Watercolour bunch of black grapes on halftone dots"></div>
    <p class="product-name">KOLTA</p>
    <p class="volume">200ml</p>
    <p class="flavour">BLACK GRAPES</p>
    <p class="tagline">fizzy drink</p>
  </section>

  <section class="label label--apple" aria-label="KOLTA red apple label">
    <div class="garnish g1" role="img" aria-label="Red apple with leaf"></div>
    <div class="garnish g2" role="img" aria-label="Red apple with leaves"></div>
    <div class="garnish g3" role="img" aria-label="Small red apple"></div>
    <div class="garnish g4" role="img" aria-label="Small red apple"></div>
    <div class="garnish g5" role="img" aria-label="Red apple with leaf"></div>
    <div class="garnish g6" role="img" aria-label="Small red apple"></div>
    <div class="garnish g7" role="img" aria-label="Red apple with leaf"></div>
    <div class="brand-tab"><span class="brand-tab__name">kestrola</span></div>
    <svg class="streaks" viewBox="0 0 186 42" aria-hidden="true"><polygon points="0,40 150,6 40,34"/><polygon points="20,42 186,2 60,34"/></svg>
    <div class="hero-fruit" role="img" aria-label="Watercolour red apple with leaf on halftone dots"></div>
    <p class="product-name">KOLTA</p>
    <p class="volume">200ml</p>
    <p class="flavour">RED APPLE</p>
    <p class="tagline">fizzy drink</p>
  </section>

</main>
</body>
</html>
```